Mega Feier am Brunnlehen - big party night in Straubing

For a party in the Anton-Velmhuber Halle in Straubing, an attractive poster for "party people" is to be created. The poster should attract at least 3000 visitors. The poster (DIN A 2) will be rebuilt by us for further use as an A5 Flyer and should thus ensure the recognition. There are no special conditions regarding colors and design - but the texts mentioned in the annex must be included. The attached photos can be used in any number and / or in excerpts (we will then insert the original high-resolution files ourselves) Important is the communication: Party Where When A reference to the KVMR as organizer is not welcome (except in the imprint) , Although the party takes place in the context of the KVMR 3-town circuit, the poster should primarily address the general party people. The fans around the rally are coming anyway. Pixel Summit - Description Date: 7th May 2018 Title: Mega Feier am Brunnlehen am 20. October 2018 possible title signature (optional, also changeable) Halle of Fame! or The hall shakes! or hall tremors with 3,000 party people or hall opening at 7 pm - open end Anton-Velmhuber Halle in Straubing Content (all 5 lines compulsory) • Cult band Gustl and the chrome bumpers • Prairie Town with DJ Rodeo shooting booths • Salon Fortuna with roulette Table • Cult figure Brezlkoenig • Large season-closing party for the KVMR 3-Orte-Fahrt Website www.3-orte-fahrt-beispiel.de Imprint: Organizer: KVMR Nordgau eV, Wendelgasse 12, 80417 Munich E-Mail: motor@ngu.kvmr-beispiel.de, Tel. : 089 - 4072 386 --------------------------------------------- ------------------------------------------ Colors: Free Format: DIN A2 logos : no font: if it is not a design element we prefer Calibri - but remains free to the designer Additional semicolons to the event (for information only): Saturday: The mega-rally party in the Velmhuber-Halle From 18 o'clock hall opening - Our Acts : - Gustl and the chrome bumpers (from 20: 30/21 clock) - Prairie Town in Foyer 2 (award ceremony KVMR eV); then open to all with Rodeo etc. (Markus is checking cooperation with Dakota Ranch) and own DJ - show involvement of Verena as a "good mood" host, especially in the time between 6pm and 9pm: Interviews, Acts or Trials the Western-Arena or the casino etc. - The "small" Auenwiesfest with dice, Hau the Luke etc.

Colors

Designer to choose colors to be used in the design.

```html
<!DOCTYPE html>
<html lang="de">
<head>
<meta charset="utf-8">
<title>Mega Feier am Brunnlehen – Plakat</title>
<link rel="stylesheet" href="https://fonts.googleapis.com/css2?family=Anton&family=Archivo+Black&family=Oswald:wght@600;700&family=Open+Sans:wght@400;600&display=swap">
<style>
  :root {
    --page: #ffffff;
    --ink: #000000;
    --sky: #1ba9e8;
    --magenta: #e6238c;
    --footer-ink: #1b1b3a;
  }
  html, body {
    margin: 0;
    padding: 0;
    width: 1200px;
    height: 823px;
    overflow: hidden;
    background: var(--page);
  }
  .poster-canvas { display: block; width: 1200px; height: 823px; }
  .headline-giant { font-family: "Anton", "Impact", sans-serif; fill: var(--ink); }
  .venue-line { font-family: "Oswald", "Arial Narrow", sans-serif; font-weight: 600; fill: var(--sky); }
  .slogan { font-family: "Archivo Black", "Arial Black", sans-serif; fill: var(--magenta); }
  .title-small { font-family: "Archivo Black", "Arial Black", sans-serif; fill: var(--ink); }
  .title-place { font-family: "Anton", "Impact", sans-serif; fill: var(--ink); }
  .program-line { font-family: "Oswald", "Arial Narrow", sans-serif; font-weight: 600; fill: var(--ink); }
  .date-line { font-family: "Oswald", "Arial Narrow", sans-serif; font-weight: 700; fill: url(#dateTone); }
  .imprint { font-family: "Open Sans", "Calibri", sans-serif; fill: var(--footer-ink); text-anchor: middle; }
  .imprint-web { font-weight: 600; }
</style>
</head>
<body>
<svg class="poster-canvas" viewBox="0 0 1500 1029" xmlns="http://www.w3.org/2000/svg">
  <defs>
    <linearGradient id="crowdTone" x1="0" y1="0" x2="1" y2="1">
      <stop offset="0" stop-color="#3aa6e0"/>
      <stop offset="0.45" stop-color="#8a4fc9"/>
      <stop offset="0.8" stop-color="#d2389a"/>
      <stop offset="1" stop-color="#4a3a9e"/>
    </linearGradient>
    <linearGradient id="stageTone" x1="0" y1="0" x2="1" y2="1">
      <stop offset="0" stop-color="#6fd0f5"/>
      <stop offset="0.4" stop-color="#3f7fd6"/>
      <stop offset="0.75" stop-color="#8f4cc6"/>
      <stop offset="1" stop-color="#c8338f"/>
    </linearGradient>
    <linearGradient id="hallTone" x1="0" y1="0" x2="1" y2="0">
      <stop offset="0" stop-color="#e0479c"/>
      <stop offset="0.5" stop-color="#9a6ad6"/>
      <stop offset="1" stop-color="#6a7fe0"/>
    </linearGradient>
    <linearGradient id="dateTone" x1="0" y1="0" x2="1" y2="0">
      <stop offset="0" stop-color="#f02f93"/>
      <stop offset="0.5" stop-color="#c06ac0"/>
      <stop offset="1" stop-color="#8a6cc8"/>
    </linearGradient>
    <clipPath id="crowdArea">
      <rect x="430" y="48" width="640" height="442"/>
    </clipPath>
    <clipPath id="sheetArea">
      <rect x="397" y="15" width="706" height="998"/>
    </clipPath>
  </defs>

  <rect class="poster-sheet" x="397" y="15" width="706" height="998" fill="var(--ink)"/>

  <g clip-path="url(#sheetArea)">
    <rect class="photo-crowd" role="img" aria-label="Photo of a crowd in a concert hall with a guitarist on stage" x="430" y="48" width="640" height="442" fill="url(#crowdTone)"/>
    <g clip-path="url(#crowdArea)">
      <text class="headline-giant" x="430" y="490" font-size="500" textLength="640" lengthAdjust="spacingAndGlyphs">MEGA</text>
    </g>

    <text class="venue-line" x="570" y="150" font-size="44">ANTON-VELMHUBER</text>
    <text class="venue-line" x="570" y="203" font-size="44">HALLE IN STRAUBING</text>
    <text class="slogan" x="493" y="285" font-size="56" textLength="515" lengthAdjust="spacingAndGlyphs">HALLE OF FAME!</text>
    <text class="venue-line" x="570" y="355" font-size="44">HALLENÖFFNUNG</text>
    <text class="venue-line" x="570" y="408" font-size="44">UM 19 UHR - OPEN END</text>

    <rect class="photo-stage" role="img" aria-label="Photo of dancing party guests with raised hands under stage lights" x="430" y="490" width="640" height="325" fill="url(#stageTone)"/>
    <text class="headline-giant" x="430" y="622" font-size="148" textLength="400" lengthAdjust="spacingAndGlyphs">FEIER</text>
    <text class="title-small" x="848" y="540" font-size="62" textLength="105" lengthAdjust="spacingAndGlyphs">am</text>
    <text class="title-place" x="848" y="620" font-size="72" textLength="222" lengthAdjust="spacingAndGlyphs">BRUNNLEHEN</text>

    <text class="program-line" x="436" y="653" font-size="26" textLength="420" lengthAdjust="spacingAndGlyphs">KULT-BAND GUSTL UND DIE CHROMSTOSSSTANGEN</text>
    <text class="program-line" x="436" y="689" font-size="26" textLength="450" lengthAdjust="spacingAndGlyphs">PRAIRIE-TOWN MIT DJ + RODEO + WURFBUDEN</text>
    <text class="program-line" x="436" y="725" font-size="26" textLength="360" lengthAdjust="spacingAndGlyphs">SALON FORTUNA MIT ROULETTE-TISCH</text>
    <text class="program-line" x="436" y="761" font-size="26" textLength="250" lengthAdjust="spacingAndGlyphs">KULT-FIGUR BREZLKOENIG</text>
    <text class="program-line" x="436" y="797" font-size="26" textLength="605" lengthAdjust="spacingAndGlyphs">GROSSE SAISON-ABSCHLUSSPARTY ZUR KVMR 3-ORTE-FAHRT</text>

    <text class="date-line" x="430" y="887" font-size="86" textLength="640" lengthAdjust="spacingAndGlyphs">am 20. oktober 2018</text>

    <rect class="photo-hall" role="img" aria-label="Photo of the event hall facade at dusk" x="430" y="904" width="640" height="76" fill="url(#hallTone)"/>
    <text class="imprint imprint-web" x="742" y="929" font-size="23">www.3-orte-fahrt-beispiel.de</text>
    <text class="imprint" x="742" y="955" font-size="18">Veranstalter: KVMR Nordgau e.V., Wendelgasse 12, 80417 München</text>
    <text class="imprint" x="742" y="977" font-size="15">E-Mail: motor@ngu.kvmr-beispiel.de, Tel.: 089 – 4072 386</text>
  </g>
</svg>
</body>
</html>
```